Tessel PR (young, fun PR agency) needs a Business Card Design

We need a new business card design that reflects who we are as a company. We're a Sydney-based PR agency that's six years old with clients including Blue Heron, Duneprint, OLVEN, Lou Carvell etc. - just check out our website for more info: www.tesselpr.com.au. We would like to see designs that bring to life our company name and what we do (generating media coverage for brands on TV, radio, online and in newspapers and magazines). We don't want a corporate style card but one that people take notice of and think 'wow that's a cool business card'. It doesn't have to be the standard rectangle shape and can incorporate humour.

Target Market(s)

Clients (generally cool/creative types) and media

Industry/Entity Type

Business

Requirements
Must have
• The card must feature our business logo (which can be updated if you like) and use both sides.
Nice to have
• The card could feature a cool illustration

```html
<!DOCTYPE html>
<html lang="en">
<head>
<meta charset="utf-8">
<title>Tessel PR – Business Card</title>
<link rel="stylesheet" href="https://fonts.googleapis.com/css2?family=Archivo+Black&family=Roboto+Slab:wght@700&family=Arimo:wght@400;700&family=Tinos:wght@700&display=swap">
<style>
  :root {
    --card-red: #ff3300;
    --card-red-deep: #e62a00;
    --accent-orange: #ff9a44;
    --panel-orange: #ffa04a;
    --ink: #000000;
    --page: #ffffff;
    --glow: #ffe6d6;
  }
  * { box-sizing: border-box; margin: 0; padding: 0; }
  html, body {
    width: 1200px; height: 373px; overflow: hidden;
    background: var(--page);
  }
  .sheet { position: relative; width: 1200px; height: 373px; }
  .side-label {
    position: absolute; top: 2px;
    font: 700 32px "Arimo", Arial, sans-serif;
    color: var(--ink);
  }
  .side-label--back { left: 10px; }
  .side-label--front { left: 574px; }

  .card {
    position: absolute; top: 46px; height: 312px;
    background: var(--card-red);
    border: 2px solid var(--ink);
    overflow: hidden;
  }
  .card--back { left: 10px; width: 537px; }
  .card--front {
    left: 574px; width: 612px;
    background: linear-gradient(90deg, var(--card-red) 0%, var(--card-red) 55%, var(--card-red-deep) 100%);
  }

  /* Back side */
  .brand {
    position: absolute; display: flex; align-items: center;
    font-family: "Archivo Black", "Arial Black", sans-serif;
    color: var(--ink); white-space: nowrap;
  }
  .card--back .brand { left: 36px; top: 28px; font-size: 44px; gap: 40px; }
  .brand-dot {
    border: 4px solid var(--ink); border-radius: 50%; display: block;
  }
  .card--back .brand-dot { width: 96px; height: 96px; }

  .contact-panel {
    position: absolute; left: 27px; top: 106px; width: 406px; height: 98px;
    background: var(--panel-orange);
    padding: 8px 12px;
    font-family: "Arimo", Arial, sans-serif; color: var(--ink);
  }
  .contact-panel .dept { font-size: 17px; font-weight: 700; line-height: 22px; }
  .contact-panel .email { font-size: 26px; line-height: 31px; }

  .tagline {
    position: absolute; left: 0; right: 0; top: 222px;
    text-align: center;
    font: 700 35px/40px "Roboto Slab", Rockwell, serif;
    color: var(--accent-orange);
  }

  /* Front side */
  .card--front .brand { left: 10px; top: 12px; font-size: 26px; gap: 14px; }
  .card--front .brand-dot { width: 54px; height: 54px; border-width: 3px; }
  .brand-sub {
    position: absolute; left: 10px; top: 48px;
    font: 700 11px "Arimo", Arial, sans-serif; color: var(--ink);
  }
  .details {
    position: absolute; left: 16px;
    font: 700 21px/26px "Tinos", "Times New Roman", serif;
    color: var(--accent-orange);
  }
  .details--phone { top: 104px; }
  .details--address { top: 202px; }

  .slogan-word {
    position: absolute; left: 290px;
    font: 700 54px/1 "Roboto Slab", Rockwell, serif;
    color: var(--accent-orange); letter-spacing: 1px;
  }
  .slogan-word--kick { top: 20px; }
  .slogan-word--ass { top: 122px; }
  .slogan-word--publicity { top: 248px; }

  .hero-art {
    position: absolute; left: 330px; top: 10px; width: 200px; height: 190px;
    background: radial-gradient(ellipse at 50% 45%, var(--glow) 0%, #ffb08a 40%, rgba(255,51,0,0) 75%);
  }
</style>
</head>
<body>
<main class="sheet">
  <h2 class="side-label side-label--back">back</h2>
  <h2 class="side-label side-label--front">Front</h2>

  <section class="card card--back">
    <div class="brand"><span>TESSEL PR</span><span class="brand-dot"></span></div>
    <div class="contact-panel">
      <p class="dept">PUBLIC RELATIONS</p>
      <p class="email">nadia@tesselpr.com.au</p>
      <p class="email">info@tesselpr.com.au</p>
    </div>
    <p class="tagline">The Top Gun in<br>Public Relations</p>
  </section>

  <section class="card card--front">
    <div class="hero-art" role="img" aria-label="Illustration of a woman in a soft white glow"></div>
    <div class="brand"><span>TESSEL PR</span><span class="brand-dot"></span></div>
    <p class="brand-sub">PUBLIC RELATIONS</p>
    <p class="details details--phone">Phone:<br>+ 61 (0)2 9000 4817</p>
    <p class="details details--address">Level 1<br>18 Harlow Street<br>Surry Hills NSW 2010</p>
    <p class="slogan-word slogan-word--kick">KICK</p>
    <p class="slogan-word slogan-word--ass">ASS</p>
    <p class="slogan-word slogan-word--publicity">PUBLICITY</p>
  </section>
</main>
</body>
</html>
```